Biz cards

Need some business cards to handout when finding clients for medical marijuana

Industry/Entity Type

Business

Contact Information for Business Card

Name: Tobin Velk
Cell #555-314-2297
Instagram: lunarharvestco

Requirements
Must have
• Needs to say ( on back of card with my info )
• MMAR Producer
• Marijuana Enthusiest and connoisseur

```html
<!DOCTYPE html>
<html lang="en">
<head>
<meta charset="utf-8">
<title>Tobin Velk – Business Card</title>
<link rel="stylesheet" href="https://fonts.googleapis.com/css2?family=Jost:wght@400;500&display=swap">
<style>
  :root {
    --teal: #13bbb8;
    --band-grey: #d1d3d4;
    --card-white: #ffffff;
    --ink: #1c1c1c;
    --backdrop: #eceae6;
  }
  html, body {
    margin: 0;
    padding: 0;
    width: 1200px;
    height: 1000px;
    overflow: hidden;
    background: var(--backdrop);
    font-family: "Jost", "Futura", sans-serif;
  }
  .canvas {
    position: relative;
    width: 1200px;
    height: 1000px;
  }
  .card {
    position: absolute;
    left: 100px;
    top: 200px;
    width: 1000px;
    height: 600px;
    background: var(--card-white);
    box-shadow: 0 4px 14px rgba(0,0,0,0.12);
  }
  .name-band {
    position: absolute;
    left: 0;
    top: 85px;
    width: 100%;
    height: 121px;
    background: var(--teal);
    display: flex;
    align-items: center;
    justify-content: center;
  }
  .name {
    margin: 0;
    color: var(--card-white);
    font-weight: 500;
    font-size: 36px;
    letter-spacing: 0.5px;
  }
  .contact-list {
    position: absolute;
    left: 480px;
    top: 276px;
    margin: 0;
    padding: 0;
    list-style: none;
  }
  .contact-item {
    display: flex;
    align-items: center;
    height: 47px;
    font-size: 29px;
    color: var(--ink);
    white-space: nowrap;
  }
  .contact-icon {
    width: 40px;
    height: 30px;
    margin-right: 25px;
    flex: none;
  }
  .address-band {
    position: absolute;
    left: 0;
    top: 463px;
    width: 100%;
    height: 50px;
    background: var(--band-grey);
    display: flex;
    align-items: center;
    justify-content: center;
  }
  .tagline {
    font-size: 29px;
    color: var(--ink);
    white-space: nowrap;
  }
</style>
</head>
<body>
<div class="canvas">
  <section class="card">
    <header class="name-band">
      <h1 class="name">TOBIN VELK</h1>
    </header>

    <ul class="contact-list">
      <li class="contact-item">
        <svg class="contact-icon" viewBox="0 0 40 30" aria-hidden="true">
          <path d="M19 3 C14 6 14 24 19 27 L22 25 L20 20 L18 20 C17 17 17 13 18 10 L20 10 L22 5 Z" fill="var(--teal)"/>
        </svg>
        <span>555-314-2297</span>
      </li>
      <li class="contact-item">
        <svg class="contact-icon" viewBox="0 0 40 30" aria-hidden="true">
          <rect x="6" y="7" width="28" height="18" fill="var(--teal)"/>
          <path d="M6 7 L20 18 L34 7" fill="none" stroke="#ffffff" stroke-width="1.6"/>
        </svg>
        <span>@lunarharvestco</span>
      </li>
      <li class="contact-item">
        <svg class="contact-icon" viewBox="0 0 40 30" aria-hidden="true">
          <g fill="none" stroke="var(--teal)" stroke-width="1.4">
            <circle cx="20" cy="15" r="11"/>
            <ellipse cx="20" cy="15" rx="5" ry="11"/>
            <line x1="9" y1="15" x2="31" y2="15"/>
            <line x1="11" y1="9" x2="29" y2="9"/>
            <line x1="11" y1="21" x2="29" y2="21"/>
          </g>
        </svg>
        <span>MMAR Producer</span>
      </li>
      <li class="contact-item">
        <svg class="contact-icon" viewBox="0 0 40 30" aria-hidden="true">
          <path d="M20 29 C14 20 12 16 12 11 A8 8 0 0 1 28 11 C28 16 26 20 20 29 Z" fill="var(--teal)"/>
          <circle cx="20" cy="11" r="3" fill="#ffffff"/>
        </svg>
        <span></span>
      </li>
    </ul>

    <footer class="address-band">
      <span class="tagline">Marijuana Enthusiast &amp; Connoisseur</span>
    </footer>
  </section>
</div>
</body>
</html>
```